Business Card Design Project

We are rebranding an existing automotive collision repair business. The business is called harrowell works. I have attached logo but I'm not tied to that. I want to leave this wide open.

I want this card to say we are professional, competent, cutting edge. We are focused on customers and use a lot of the latest technology to make the customer experience different. We sign customers in on Vextabs. Paperwork I signed electronically and updates are sent via text, email, logging on a website or as they wish. I want this innovation and image to come through in our cards

Target Market(s)

60%. Women 40% men. Age 35-60

Industry/Entity Type

Automotive

Requirements
Must have
• The card must have name, title, phone,email, cell, web page

```html
<!DOCTYPE html>
<html lang="en">
<head>
<meta charset="utf-8">
<title>harrowell works — Business Card</title>
<link rel="stylesheet" href="https://fonts.googleapis.com/css2?family=Open+Sans:wght@400;700&display=swap">
<style>
  :root {
    --canvas-bg: #e4e6e3;
    --card-white: #ffffff;
    --green-deep: #1f7d2b;
    --green-mid: #4ea32a;
    --green-light: #82c226;
    --text-grey: #6d6d6d;
    --text-dark: #111111;
    --stripe-grey: #b9b9b9;
    --stripe-dark: #2a2a2a;
  }
  * { box-sizing: border-box; margin: 0; padding: 0; }
  html, body {
    width: 1200px; height: 900px; overflow: hidden;
    background: var(--canvas-bg);
    font-family: "Open Sans", Arial, sans-serif;
  }
  .canvas {
    position: relative; width: 1200px; height: 900px;
  }
  .card {
    position: absolute; left: 250px; width: 700px; height: 400px;
    border-radius: 30px; overflow: hidden;
    box-shadow: 0 6px 18px rgba(0,0,0,0.18);
  }
  .card-front { top: 40px; background: var(--card-white); }
  .card-back {
    top: 470px;
    background: linear-gradient(100deg, var(--green-deep) 0%, var(--green-mid) 50%, var(--green-light) 100%);
  }

  /* front */
  .front-swoosh { position: absolute; inset: 0; width: 700px; height: 400px; }
  .brand {
    position: absolute; left: 44px; top: 34px;
    display: flex; align-items: center; gap: 10px;
  }
  .brand-dot {
    width: 16px; height: 16px; border-radius: 50%; background: var(--green-mid);
  }
  .brand-name {
    font-weight: 700; font-size: 30px; color: var(--green-mid); letter-spacing: 0.2px;
  }
  .address {
    position: absolute; left: 48px; top: 96px;
    font-size: 15px; line-height: 21px; color: var(--text-grey);
  }
  .contact-list {
    position: absolute; left: 48px; top: 150px; list-style: none;
    font-size: 15px; line-height: 22px; color: var(--text-grey);
  }
  .contact-list li { display: flex; align-items: center; gap: 9px; }
  .contact-icon { width: 13px; height: 13px; flex: none; }
  .person {
    position: absolute; right: 70px; top: 254px; text-align: left;
  }
  .person-name { font-weight: 700; font-size: 24px; color: var(--text-dark); }
  .person-title { font-size: 16px; color: var(--text-grey); margin-left: 40px; }

  /* back */
  .back-brand {
    position: absolute; left: 0; right: 0; top: 150px;
    display: flex; justify-content: center; align-items: center; gap: 14px;
  }
  .back-brand .brand-dot { width: 22px; height: 22px; background: #ffffff; }
  .back-brand-name { font-weight: 700; font-size: 46px; color: #ffffff; }
  .back-web {
    position: absolute; left: 0; right: 0; top: 300px; text-align: center;
    font-size: 19px; color: #ffffff; letter-spacing: 0.5px;
  }
</style>
</head>
<body>
<main class="canvas">

  <section class="card card-front" aria-label="Card front">
    <svg class="front-swoosh" viewBox="0 0 700 400" aria-hidden="true">
      <defs>
        <linearGradient id="swooshGreen" x1="0" y1="0" x2="1" y2="0">
          <stop offset="0" stop-color="#82c226"/>
          <stop offset="0.45" stop-color="#1f7d2b"/>
          <stop offset="1" stop-color="#82c226"/>
        </linearGradient>
      </defs>
      <path d="M0,222 C170,300 420,355 700,372 L700,400 L0,400 Z" fill="url(#swooshGreen)"/>
      <path d="M0,232 C180,306 430,356 700,368" fill="none" stroke="#b9b9b9" stroke-width="10"/>
      <path d="M0,228 C180,300 430,350 700,362" fill="none" stroke="#2a2a2a" stroke-width="2"/>
    </svg>

    <div class="brand">
      <span class="brand-dot"></span>
      <span class="brand-name">harrowell works</span>
    </div>

    <p class="address">4170 W. Larkspur Drive. STE 12<br>PMB#310 Tempe, AZ 85281</p>

    <ul class="contact-list">
      <li>
        <svg class="contact-icon" viewBox="0 0 16 16" aria-hidden="true"><path d="M3 1l3 3-1.5 2c1 2 3 4 5 5L11.5 9.5l3 3L13 15C7 14 2 9 1 3z" fill="#4ea32a"/></svg>
        800-555-0142
      </li>
      <li>
        <svg class="contact-icon" viewBox="0 0 16 16" aria-hidden="true"><rect x="1" y="10" width="3" height="5" fill="#4ea32a"/><rect x="6" y="6" width="3" height="9" fill="#4ea32a"/><rect x="11" y="2" width="3" height="13" fill="#4ea32a"/></svg>
        800-555-0142
      </li>
      <li>
        <svg class="contact-icon" viewBox="0 0 16 16" aria-hidden="true"><rect x="1" y="3" width="14" height="10" fill="none" stroke="#4ea32a" stroke-width="1.6"/><path d="M1 3l7 6 7-6" fill="none" stroke="#4ea32a" stroke-width="1.6"/></svg>
        info@harrowellworks.com
      </li>
      <li>
        <svg class="contact-icon" viewBox="0 0 16 16" aria-hidden="true"><circle cx="8" cy="8" r="6.5" fill="none" stroke="#4ea32a" stroke-width="1.5"/><path d="M1.5 8h13M8 1.5c-3 3-3 10 0 13M8 1.5c3 3 3 10 0 13" fill="none" stroke="#4ea32a" stroke-width="1.2"/></svg>
        www.harrowellworks.com
      </li>
    </ul>

    <div class="person">
      <p class="person-name">Jordan Hale</p>
      <p class="person-title">Vice President</p>
    </div>
  </section>

  <section class="card card-back" aria-label="Card back">
    <div class="back-brand">
      <span class="brand-dot"></span>
      <span class="back-brand-name">harrowell works</span>
    </div>
    <p class="back-web">www.harrowellworks.com</p>
  </section>

</main>
</body>
</html>
```